Flyer Design for Southern Guild of Mindful Listeners and Carers (SGMLC)

We need a new flyer designed for SGMLC. We want to attract new members @ a tradeshow. Counsellors and Psychotherapists looking for a professional association with which to align themselves where they feel @ home because they share similar values.We would like to use the colours and leaves from our website which is www.sgmlc-guild.org if possible or similar colours and the photo of the tree in bloom from Facebook "stillwaterandcarework". As well as our logo (www.sgmlc-guild.org), the TOVRE (www.tovre-hub.org) logo as well somewhere in the bottom corner the Quiet Path Forum logo (www.quietpathforum.org).

Target Market(s)

Psychotherapists and Counsellors

Industry/Entity Type

Mental Health

Colors
876aae
b7a5cd
e4daeb
cadf82
abd036
9bcb3b

Requirements
Must have
• Logo
Nice to have
• Warm inviting photo of lotus flower
Should not have
• No monks

```html
<!DOCTYPE html>
<html lang="en">
<head>
<meta charset="utf-8">
<title>SGMLC Flyer</title>
<link rel="stylesheet" href="https://fonts.googleapis.com/css2?family=Arimo:wght@400;700&display=swap">
<style>
:root{
  --purple:#876aae;
  --lavender:#b7a5cd;
  --mist:#e4daeb;
  --lime:#cadf82;
  --green:#abd036;
  --leaf:#9bcb3b;
  --ink:#1e1a22;
  --page:#ececec;
  --card:#ffffff;
}
*{box-sizing:border-box;margin:0;padding:0}
html,body{width:869px;height:1200px;overflow:hidden}
body{background:var(--page);font-family:"Arimo",Arial,sans-serif;color:var(--ink);position:relative}
.sheet{position:absolute;left:68px;width:733px;background:var(--card);overflow:hidden}
.sheet--front{top:52px;height:541px}
.sheet--back{top:625px;height:518px}
.sheet__shapes{position:absolute;inset:0;width:100%;height:100%}
.brand{position:absolute;display:flex;flex-direction:column;align-items:center;gap:6px;color:var(--ink);font-weight:400}
.brand__name{font-size:16px;letter-spacing:.5px}
.brand__mark{width:36px;height:36px;border-radius:50%;background:var(--ink)}
.brand--front{left:40px;top:22px}
.brand--back{left:615px;top:322px}
.brand--back .brand__name{font-size:20px}
.site-url{position:absolute;left:24px;top:104px;font-size:12.5px;font-weight:700}
.art{position:absolute}
.art--lotus{left:232px;top:12px;width:320px;height:196px;border-radius:50% 50% 45% 45%;
  background:radial-gradient(ellipse at 50% 45%,#f7c25a 0%,#8bc9ea 30%,#d55aa0 55%,rgba(240,225,215,.6) 75%,rgba(255,255,255,0) 80%)}
.art--leaves{left:0;top:400px;width:733px;height:141px;
  background:linear-gradient(90deg,rgba(228,218,235,.9),rgba(202,223,130,.35) 55%,rgba(183,165,205,.55))}
.art--dots{left:470px;top:0;width:263px;height:60px;
  background:linear-gradient(90deg,rgba(255,255,255,0),rgba(200,200,200,.55))}
.art--flower{left:0;top:180px;width:440px;height:240px;
  background:radial-gradient(ellipse at 45% 55%,rgba(233,169,200,.85) 0%,rgba(240,200,220,.55) 40%,rgba(255,255,255,0) 72%)}
.band{position:absolute;left:0;width:733px}
.band--vision{top:264px;height:113px;background:linear-gradient(90deg,rgba(228,218,235,.95),rgba(228,218,235,.55))}
.band--values{top:377px;height:164px;background:linear-gradient(90deg,rgba(228,218,235,.7),rgba(228,218,235,.35))}
.tab{position:absolute;left:21px;height:30px;padding:0 30px 0 12px;color:#fff;font-size:19px;font-weight:400;line-height:30px;white-space:nowrap;
  clip-path:polygon(0 0,100% 0,calc(100% - 18px) 100%,0 100%)}
.tab--purple{background:var(--purple)}
.tab--green{background:var(--green)}
.rule{position:absolute;left:0;height:2px;width:733px}
.rule--purple{background:var(--purple)}
.rule--green{background:var(--green)}
.copy{position:absolute;left:10px;width:706px;font-size:10.2px;line-height:13.4px}
.list{position:absolute;left:30px;width:640px;list-style:none;font-size:10.2px;line-height:12.8px}
.list li{position:relative;padding-left:16px}
.list li::before{content:"";position:absolute;left:0;top:2px;width:8px;height:8px;border:1px solid #555;border-radius:50%;background:#fff}
.list--values li{margin-bottom:7.5px}
.list--objectives li{margin-bottom:6.8px}
.footer-band{position:absolute;left:0;top:416px;width:733px;height:12px;background:linear-gradient(var(--purple) 0 5px,var(--mist) 5px)}
.contact{position:absolute;font-size:10px;line-height:11.5px}
.contact__org{color:var(--purple);font-weight:700;margin-bottom:8px}
.contact--main{left:13px;top:433px}
.contact--main p:last-child{font-weight:700}
.contact--branch{left:480px;top:453px}
.contact--branch .contact__org{margin-bottom:0}
</style>
</head>
<body>

<section class="sheet sheet--front">
  <svg class="sheet__shapes" viewBox="0 0 563 415" preserveAspectRatio="none" aria-hidden="true">
    <polygon points="505,0 563,0 563,18 350,265 300,265" fill="#e4daeb"/>
    <polygon points="563,32 563,185 430,185" fill="#cadf82"/>
    <polygon points="563,200 563,415 470,415" fill="#e4daeb" opacity=".8"/>
  </svg>
  <div class="brand brand--front"><span class="brand__name">SGMLC</span><span class="brand__mark"></span></div>
  <div class="site-url">www.sgmlc-guild.org</div>
  <div class="art art--lotus" role="img" aria-label="Illustrated lotus flower with orange, green, blue and pink petals above rippling water"></div>

  <div class="band band--vision"></div>
  <div class="rule rule--purple" style="top:264px"></div>
  <div class="tab tab--purple" style="top:234px">Our Vision</div>
  <p class="copy" style="top:271px">The purpose of The Southern Guild of Mindful Listeners and Carers (SGMLC), a TOVRE Member Association, is to bring the whole philosophy and practice of Buddhism (the dhamma), totherapists and counsellors, using innovative educational experiences. The benefits of introducing Buddhist practices into mental health is now scientifically validated, as increasing the effectiveness of Western psychotherapeutic approaches, as well as taking care of therapists in particular 'burnout.'<br>There is much to benefit us, as well as those we work with, in our desire to integrate Psychotherapy with Buddhism. So, SGMLC has developed and has been runninga two-year professional training course in Buddhism and Psychotherapy, since 2008.The next training will begin July 2016.</p>

  <div class="band band--values"></div>
  <div class="art art--leaves" role="img" aria-label="Soft background of green leaves"></div>
  <div class="rule rule--green" style="top:407px"></div>
  <div class="tab tab--green" style="top:378px">Some of Our Values</div>
  <ul class="list list--values" style="top:419px">
    <li>We care about therapists</li>
    <li>We strive to be of service to our members and all those we come into contact with humility, fairness, patience and compassion</li>
    <li>We value the ongoing need for education for therapists but we also value the balance between the mind, the body and the spirit, knowing that all those need to be nourished</li>
    <li>We work in warm, generous, spirited partnership with others and we are open to working within and across sectors to influence and co-develop initiatives.</li>
  </ul>
</section>

<section class="sheet sheet--back">
  <div class="art art--dots" role="img" aria-label="Fading halftone dot pattern"></div>
  <svg class="sheet__shapes" viewBox="0 0 563 397" preserveAspectRatio="none" aria-hidden="true">
    <polygon points="563,95 563,140 340,322 270,322" fill="#e4daeb"/>
    <polygon points="563,150 563,265 450,265" fill="#cadf82"/>
    <polygon points="563,265 563,322 480,322" fill="#e4daeb"/>
  </svg>
  <div class="art art--flower" role="img" aria-label="Soft photograph of a pink lotus flower in bloom"></div>
  <div class="brand brand--back"><span class="brand__name">SGMLC</span><span class="brand__mark"></span></div>

  <div class="rule rule--purple" style="top:62px"></div>
  <div class="tab tab--purple" style="top:33px">Objectives</div>
  <ul class="list list--objectives" style="top:72px">
    <li>To provide a philosophical base,standardsand ethics for the practice of Buddhist Counselling and Psychotherapy.</li>
    <li>Maintain unique professional development of its members, as well as provide a warm and supportive community of therapists.</li>
    <li>Develop a professional organisational structure that supports the practice of Buddhist Counselling and Psychotherapy;</li>
    <li>Provide an innovative education, training and research in Buddhist Counselling and Psychotherapy;</li>
    <li>Promote Buddhist Counselling and Psychotherapy in the community;</li>
    <li>Provide accreditation practices that will support the highest quality practice in Buddhist Counselling and Psychotherapy; and</li>
    <li>Work collaboratively and beneficially with other Buddhist and Counselling and Psychotherapy Organisations.</li>
  </ul>

  <div class="rule rule--green" style="top:244px"></div>
  <div class="tab tab--green" style="top:215px">Objectives</div>
  <ul class="list list--objectives" style="top:255px">
    <li>To present Buddhism in a through way</li>
    <li>To explore and discuss dhamma and how it can improve the effectiveness of a therapist's life</li>
    <li>To provide ongoing education in all aspects of Buddhism for mental health professionals</li>
    <li>To develop a dynamic organisation that stays attuned to changes in Buddhism as it is expressed in the West</li>
    <li>To develop a strong membership/community</li>
    <li>To develop a relevant and important voice in the community</li>
    <li>To develop a unique professional identity</li>
    <li>To encourage positive social change</li>
  </ul>

  <div class="footer-band"></div>
  <div class="contact contact--main">
    <p class="contact__org">Southern Guild of Mindful Listeners<br>and Carers</p>
    <p>PO Box 4820<br>Harlow Point 2718 NSW<br>Australia<br>Email: info@stillwaterandcarework.org</p>
  </div>
  <div class="contact contact--branch">
    <p class="contact__org">Southern Guild of Mindful Listeners<br>and Carers</p>
    <p>Queensland Branch<br>Email: qld@stillwaterandcarework.org</p>
  </div>
</section>

</body>
</html>
```